Brightwell Polar Systems Inc.
Business Card, Letter Head, Fax Cover, evelope and T-shirt
Bright & Fun-filled
Dorian Kestle
342 Harrowgate Ave
Cedarbrook, PA, 19095
dkestle@bpsyst.example
www.Bpsyst.example
ill be using a clear plastic card, but also lets have the background as black.
Heating
Air Condition
Ventilation
Duct Work
Refrigeration
Solar, Geothermal
Design, Fabrication & Installation
Sales, Service & Repair

```html
<!DOCTYPE html>
<html lang="en">
<head>
<meta charset="utf-8">
<title>Brightwell Polar Systems Inc. – Business Card</title>
<link rel="stylesheet" href="https://fonts.googleapis.com/css2?family=Cinzel:wght@400;600&display=swap">
<style>
  :root{
    --page:#d8d8d8;
    --card-dark:#141414;
    --card-dark-2:#2b2b2b;
    --blue-light:#5fd0ef;
    --blue-deep:#1596c4;
    --green:#3fae3a;
    --green-light:#9be06a;
    --brand-green:#46b03c;
    --mark-orange:#e8561c;
    --web-red:#d8261c;
    --ink-dark:#0d2533;
    --white:#ffffff;
  }
  *{margin:0;padding:0;box-sizing:border-box}
  html,body{width:1200px;height:862px;overflow:hidden;background:var(--page)}
  body{position:relative;font-family:"Cinzel",serif}
  .card{position:absolute;width:560px;height:320px;border-radius:16px;overflow:hidden;
        box-shadow:0 8px 22px rgba(0,0,0,.35)}
  .card svg.card-bg{position:absolute;inset:0}
  .card-front{left:130px;top:80px}
  .card-back{left:510px;top:462px}

  .brand{position:absolute;display:flex;align-items:center;gap:14px}
  .brand-dot{width:70px;height:70px;border-radius:50%;background:var(--mark-orange);flex:none}
  .brand-name{color:var(--brand-green);font-weight:600;font-size:26px;line-height:1.05;letter-spacing:.5px}
  .card-front .brand{left:22px;top:18px}
  .card-back .brand{left:300px;top:170px}
  .card-back .brand-dot{width:62px;height:62px}
  .card-back .brand-name{font-size:19px}

  .holder-name{position:absolute;left:24px;top:116px;color:var(--white);font-size:22px;font-weight:400;letter-spacing:.5px}
  .address{position:absolute;right:24px;top:142px;text-align:right;color:var(--white);font-size:13px;line-height:1.3}
  .phones{position:absolute;right:24px;top:190px;text-align:right;color:var(--ink-dark);font-size:13px;line-height:1.3}
  .web-contacts{position:absolute;left:24px;top:210px;color:var(--ink-dark);font-size:11.5px;line-height:1.35}

  .services{position:absolute;left:22px;top:20px;list-style:none;color:var(--white);font-size:12px;line-height:1.55}
  .services li span{margin-right:8px}
  .services li span::before{content:"\2022\00a0"}
  .back-web{position:absolute;right:24px;bottom:18px;color:var(--web-red);font-size:18px}
</style>
</head>
<body>

<section class="card card-front" aria-label="Business card front">
  <svg class="card-bg" width="560" height="320" viewBox="0 0 560 320">
    <defs>
      <linearGradient id="front-dark" x1="0" y1="0" x2="1" y2="1">
        <stop offset="0" stop-color="var(--card-dark-2)"/>
        <stop offset="1" stop-color="var(--card-dark)"/>
      </linearGradient>
      <linearGradient id="front-blue" x1="0" y1="0" x2="0" y2="1">
        <stop offset="0" stop-color="var(--blue-light)"/>
        <stop offset="1" stop-color="var(--blue-deep)"/>
      </linearGradient>
      <linearGradient id="front-stripe" x1="0" y1="0" x2="1" y2="0">
        <stop offset="0" stop-color="var(--green)"/>
        <stop offset=".5" stop-color="var(--green-light)"/>
        <stop offset="1" stop-color="var(--green)"/>
      </linearGradient>
    </defs>
    <rect width="560" height="320" fill="url(#front-dark)"/>
    <path d="M0,172 C160,152 330,182 560,108 L560,320 L0,320 Z" fill="url(#front-blue)"/>
    <path d="M0,160 C160,140 330,170 560,96" fill="none" stroke="url(#front-stripe)" stroke-width="9"/>
    <path d="M0,168 C160,148 330,178 560,104" fill="none" stroke="var(--white)" stroke-width="1.5" opacity=".8"/>
  </svg>

  <div class="brand">
    <span class="brand-dot"></span>
    <span class="brand-name">Brightwell Polar<br>Systems Inc.</span>
  </div>

  <p class="holder-name">Dorian Kestle</p>
  <p class="address">342 Harrowgate Ave<br>Cedarbrook, PA, 19095</p>
  <p class="phones">718-555-0186 P.<br>646-555-0129 C.<br>718-555-0180 F.</p>
  <p class="web-contacts">E. dkestle@bpsyst.example<br>W. www.Bpsyst.example</p>
</section>

<section class="card card-back" aria-label="Business card back">
  <svg class="card-bg" width="560" height="320" viewBox="0 0 560 320">
    <defs>
      <linearGradient id="back-dark" x1="0" y1="0" x2="1" y2="1">
        <stop offset="0" stop-color="var(--card-dark-2)"/>
        <stop offset="1" stop-color="var(--card-dark)"/>
      </linearGradient>
      <linearGradient id="back-blue" x1="0" y1="0" x2="0" y2="1">
        <stop offset="0" stop-color="var(--blue-deep)"/>
        <stop offset="1" stop-color="var(--blue-light)"/>
      </linearGradient>
      <linearGradient id="back-stripe" x1="0" y1="0" x2="1" y2="0">
        <stop offset="0" stop-color="var(--green)"/>
        <stop offset=".5" stop-color="var(--green-light)"/>
        <stop offset="1" stop-color="var(--green)"/>
      </linearGradient>
    </defs>
    <rect width="560" height="320" fill="url(#back-dark)"/>
    <path d="M0,0 L560,0 L560,100 C380,150 200,96 0,150 Z" fill="url(#back-blue)"/>
    <path d="M0,158 C200,104 380,158 560,108" fill="none" stroke="url(#back-stripe)" stroke-width="9"/>
    <path d="M0,151 C200,97 380,151 560,101" fill="none" stroke="var(--white)" stroke-width="1.5" opacity=".8"/>
  </svg>

  <ul class="services">
    <li><span>Heating</span><span>Air Condition</span></li>
    <li><span>Ventilation</span><span>Duct Work</span><span>Refrigeration</span><span>Solar, Geothermal</span></li>
    <li><span>Design, Fabrication &amp; Installation</span></li>
    <li><span>Sales, Service &amp; Repair</span></li>
  </ul>

  <div class="brand">
    <span class="brand-dot"></span>
    <span class="brand-name">Brightwell Polar<br>Systems Inc.</span>
  </div>

  <p class="back-web">www.Bpsyst.example</p>
</section>

</body>
</html>
```